Solar lighting products series needs packaging design

We are developing and selling Solar lighting solutions to African markets.
Currently we have too many designs and each product has unprofessional design, which makes products looks cheap, although our products are very good.

We want to make packaging design for our products with the same logic and style, and few differences due to product type, and packaging sizes.
We currently have five products in our portfolio, corresponding to 3 families of products:
- Solar torch light: Korvu.Ta Heron v.1
- Solar Lights : Korvu.Ta Puma v.1, Korvu.Ta Ocelot v.1, Korvu.Ta Serval v.1
- Mini-Solar System : Korvu.Ta Gaur v.1
Each family is representing by a category of animals:
- Solar Torch Light by birds (since those are mobile lighting systems),
- Solar Lights by felids (since those are prestigious lighting systems),
- Mini-Solar System by cattle (since those are not mobile lighting systems, and this family is dedicated to rural areas),

We need to have a packaging design with the same logic and design style inspired by our logo.

Target Market(s)

African Markets - decision taker (adults - 30/60 years old)
Prestigious object

Industry/Entity Type

Product

Requirements
Must have
• Korvu.Ta Puma v.1, Korvu.Ta Ocelot v.1, Korvu.Ta Serval v.1 and Korvu.Ta Gaur v.1 packaging must have the following details:
Front side:
- Brand logo,
- Brand slogan EN & FR,
o Bright Power at Every Door!
o Le Courant Clair Chez Chacun !
- Product name,
- Short Product description EN & FR, (2 lines space)
- Designed quality and specificities Labels EN / FR :
o Battery capacity
o Solar module capacity
o Lightning brightness
o Numbers of LEDs
o Lights modes
o USB port
o Mobile Phone Charging
o Warranty length in months
o Battery deposit refund system
- Website address,
- Designed product (no picture but the draw designed shape of the product is needed),
- Designed animal corresponding to the name of the product on the background in transparency,
- Conception / Design 100% Afrique / Africa
Back side: (you can maybe divide the backside in four different spaces)
- Brand logo,
- Brand slogan EN & FR,
- Product name,
- Designed quality and specificities Labels EN / FR and descriptions EN / FR:
o Battery capacity (4 lines spaces)
o Solar module capacity (2 lines spaces)
o Lightning brightness (2 lines spaces)
o Numbers of LEDs (2 lines spaces)
o Lights modes (2 lines spaces)
o USB port (2 lines spaces)
o Mobile Phone Charging (2 lines spaces)
o Warranty length in months (2 lines spaces)
o Battery deposit refund system (4 lines spaces)
- Designed object (no picture but the draw designed shape of the product is needed),
- Usage design shadow in situation, (with 2 people shape in black color and the product shape in a distinct color)
- List of 5 reasons to buy FR / EN :
o 1: (4 lines spaces)
o 2: (4 lines spaces)
o 3: (4 lines spaces)
o 4: (4 lines spaces)
o 5: (4 lines spaces)
- Design / Conception 100% Afrique / 100% Africa with African continent drawing
- Fabriqué en RPC / Made in PRC
- Website address,
Right Side:
- Brand logo,
- Brand slogan EN & FR,
- Product name,
- Website address,
- CE logo / RoHs logo / Recycling logo / Don’t throw in rubbish logo
- Industry association logos: http://www.brevomarel.org/ / http://quintarvelomunionsociety.org/
- Copyright © year, Korvu.Ta
- All rights reserved.
- Distributed by : ‘place for a sticker’
- Serial number / numéro de série : ‘place for a sticker’
- Conception 100% Afrique / Design 100% Africa
- Included: “designed drawing of included pieces (4 square spaces for further drawing)”
Side 2:
- Brand logo,
- Brand slogan EN & FR,
- Product name,
- Website address,
- Technical Datasheet EN / FR (14 lines / 2 columns):
o Table with: Light technology / Max. Lumen Output / Lights modes / Battery / Battery Cycles / Lamp Input / Lamp Output / Solar Panel / Solar Charge Duration / Autonomy modes / Certificates / Limited Warranty / Weight / Waterproof
- Usage Manual EN / FR:
o How to use EN / FR (leave 8 lines space)
o How to charge EN / FR (leave 4 lines space)
o Solar Panel maintenance EN / FR (leave 4 lines space)
o Battery maintenance EN / FR (leave 8 lines space)
o Limited Warranty instructions EN / FR (leave 10 lines space)
Top-Side
- Brand logo,
- Brand slogan EN & FR,
- Product name,
- Website address,
Down-Side
- Brand logo,
- Brand slogan EN & FR,
- Product name,
- Website address,
- Designed animal corresponding to the name of the product,

Korvu.Ta Heron v.1 due to its size limitation should have a packaging inspired by other product packaging / the rest of information will be insert in printed manual notice.
Nice to have
• Each family of product should have a color differentiation.

```html
<!DOCTYPE html>
<html lang="en">
<head>
<meta charset="utf-8">
<title>Korvu.Ta Solar Lantern – Packaging Dieline</title>
<link rel="stylesheet" href="https://fonts.googleapis.com/css2?family=Open+Sans:ital,wght@0,400;0,600;0,700;0,800;1,600;1,700;1,800&display=swap">
<style>
:root{
  --canvas:#ebebeb;
  --flap-blue:#2a5a95;
  --panel-blue:#2d5b96;
  --navy:#1d2f55;
  --head-blue:#3b5f93;
  --band-top:#d3dbe1;
  --band-bottom:#eef1f3;
  --tuck-grey:#8d8d8d;
  --tuck-grey-dark:#7a7a7a;
  --side-dark:#353535;
  --runtime-red:#990000;
  --foot-pink:#cbb0b5;
  --brand-red:#b3161b;
  --sun-orange:#f5a416;
  --white:#ffffff;
  --sky:#3f86cf;
  --grass:#5aa33a;
}
*{margin:0;padding:0;box-sizing:border-box}
html,body{width:1200px;height:857px;overflow:hidden;background:var(--canvas);font-family:"Open Sans",Arial,sans-serif}
.canvas{position:relative;width:1200px;height:857px}
.abs{position:absolute}

/* flaps */
.top-flap{background:var(--flap-blue)}
.tuck-flap{overflow:visible}

/* brand */
.brand{display:flex;align-items:center;gap:6px;justify-content:center}
.brand-dot{width:26px;height:26px;border-radius:50%;background:var(--sun-orange)}
.brand-name{font-weight:800;font-size:17px;color:var(--brand-red)}
.flap-web{font-weight:700;font-size:10px;color:#111;text-align:center}

/* body */
.glue-edge{left:45px;top:298px}
.band-top{background:linear-gradient(180deg,var(--band-top),var(--band-bottom))}
.band-foot{background:linear-gradient(180deg,#c9cdd1,#e7e9eb)}
.photo-scene{background:linear-gradient(180deg,#2f6fbd 0%,var(--sky) 30%,#cfe3f3 55%,#8cc457 62%,var(--grass) 100%)}
.lamp-photo{background:radial-gradient(ellipse at 50% 45%,#f3f3ee 0%,#e9e3b0 40%,rgba(245,205,20,.85) 62%,rgba(40,40,40,.6) 90%,rgba(0,0,0,0) 100%);border-radius:30px}
.side-strip{background:linear-gradient(90deg,#222,var(--side-dark) 50%,#4a4a4a)}

.front-tagline{font-weight:800;font-style:italic;font-size:16.5px;line-height:20px;color:var(--head-blue);text-shadow:2px 2px 3px rgba(0,0,0,.35);letter-spacing:.2px}
.front-slogan{font-weight:800;font-style:italic;font-size:17px;color:var(--navy);text-shadow:2px 2px 3px rgba(0,0,0,.35)}
.spec-list{list-style:none;font-weight:700;font-size:12.5px;line-height:19.5px;color:var(--navy)}
.spec-list li::before{content:"o ";font-weight:600}
.foot-web{font-weight:700;font-size:10px;color:#111}
.badge{width:34px;height:34px;background:#111;border:2px solid #fff;outline:1px solid #666}
.badge.amber{background:#b54a12;border-radius:50%}
.badge.green{background:#6a7b2c}
.foot-slogan{font-weight:700;font-style:italic;font-size:13px;line-height:18px;color:#fff;text-shadow:1px 1px 2px rgba(0,0,0,.5)}

/* back panel */
.info-blue{background:var(--panel-blue)}
.back-slogan{font-weight:700;font-style:italic;font-size:12px;line-height:17px;color:#fff}
.back-item{font-weight:700;font-size:11.5px;color:#fff;line-height:14.5px}
.back-item::before{content:"o ";font-weight:600}
.back-note{font-weight:600;font-size:5.5px;line-height:7px;color:#fff}
.spec-table{border-collapse:collapse;background:#fff;font-size:4.8px;color:#222;width:212px}
.spec-table td,.spec-table th{border:.5px solid #999;padding:0 3px;height:8px;font-weight:400;text-align:left}
.africa-note{font-weight:700;font-style:italic;font-size:7.5px;line-height:10px;color:#fff}
.back-web{font-weight:700;font-size:11px;color:#fff}
.band-pink{background:var(--foot-pink)}
.origin-note{font-weight:700;font-style:italic;font-size:7.5px;line-height:10px;color:#222}

/* runtime panel */
.runtime-red{background:var(--runtime-red)}
.runtime-title{font-weight:800;font-size:13px;color:#111}
.runtime-text{font-weight:600;font-size:5.6px;line-height:7.5px;color:#fff}
.callout{font-weight:600;font-size:7px;color:#fff}
.runtime-foot{font-weight:700;font-style:italic;font-size:6.6px;line-height:9px;color:#fff}
</style>
</head>
<body>
<div class="canvas">

  <!-- top flaps -->
  <div class="abs top-flap" style="left:95px;top:38px;width:262px;height:260px">
    <div class="brand abs" style="left:0;right:0;top:110px"><span class="brand-dot"></span><span class="brand-name">Korvu.Ta</span></div>
    <div class="flap-web abs" style="left:0;right:0;top:213px">www.brevomarel.org</div>
  </div>
  <svg class="abs tuck-flap" style="left:361px;top:170px" width="252" height="128" viewBox="0 0 252 128">
    <defs><linearGradient id="tuck" x1="0" y1="0" x2="0" y2="1"><stop offset="0" stop-color="#9a9a9a"/><stop offset="1" stop-color="#7d7d7d"/></linearGradient></defs>
    <path d="M0 8 Q0 0 8 0 H190 Q198 0 198 8 V14 Q198 22 206 22 H230 Q238 22 238 30 V128 H0 Z" fill="url(#tuck)"/>
  </svg>

  <div class="abs top-flap" style="left:619px;top:38px;width:262px;height:260px">
    <div class="brand abs" style="left:0;right:0;top:110px"><span class="brand-dot"></span><span class="brand-name">Korvu.Ta</span></div>
  </div>
  <svg class="abs tuck-flap" style="left:884px;top:170px" width="262" height="128" viewBox="0 0 262 128">
    <path d="M0 8 Q0 0 8 0 H196 Q204 0 204 8 V14 Q204 22 212 22 H240 Q248 22 248 30 V128 H0 Z" fill="url(#tuck)"/>
  </svg>

  <!-- glue edge -->
  <svg class="abs glue-edge" width="50" height="512" viewBox="0 0 50 512">
    <defs><linearGradient id="glue" x1="0" y1="0" x2="1" y2="0"><stop offset="0" stop-color="#1a1a1a"/><stop offset="1" stop-color="#3c3c3c"/></linearGradient></defs>
    <polygon points="0,24 50,0 50,512 0,502" fill="url(#glue)"/>
  </svg>

  <!-- front panels -->
  <div class="abs band-top" style="left:95px;top:298px;width:518px;height:101px"></div>
  <div class="abs photo-scene" role="img" aria-label="Photo of a sunny sky over a green meadow" style="left:95px;top:399px;width:518px;height:339px"></div>
  <div class="abs lamp-photo" role="img" aria-label="Photo of the yellow solar lantern with its solar panel lid open" style="left:405px;top:485px;width:160px;height:225px"></div>
  <svg class="abs" style="left:95px;top:660px" width="262" height="78" viewBox="0 0 262 78">
    <polygon points="0,35 262,8 215,78 0,78" fill="#fff" opacity=".55"/>
  </svg>

  <div class="abs front-tagline" style="left:105px;top:345px">ENERGY- DURABILITY-<br>HILIGHT- EYESHIELD</div>
  <div class="abs front-slogan" style="left:377px;top:339px">Bright Power at Every Door!</div>

  <ul class="abs spec-list" style="left:128px;top:578px">
    <li>Battery capacity</li>
    <li>Solar module capacity</li>
    <li>Lightning brightness</li>
    <li>Numbers of LEDs</li>
    <li>Lights modes</li>
    <li>USB port</li>
    <li>Mobile Phone Charging</li>
    <li>Warranty length in months</li>
    <li>Battery deposit refund system</li>
  </ul>

  <div class="abs band-foot" style="left:95px;top:738px;width:518px;height:72px"></div>
  <div class="abs foot-web" style="left:144px;top:741px">www.brevomarel.org</div>
  <div class="abs badge" style="left:127px;top:757px"></div>
  <div class="abs badge amber" style="left:186px;top:757px"></div>
  <div class="abs badge green" style="left:231px;top:757px"></div>
  <div class="abs foot-slogan" style="left:400px;top:750px">o Bright Power at Every Door!<br>o Le Courant Clair Chez Chacun !</div>

  <div class="abs side-strip" style="left:613px;top:298px;width:32px;height:512px"></div>

  <!-- back panel -->
  <div class="abs band-top" style="left:645px;top:298px;width:236px;height:101px">
    <div class="brand abs" style="left:0;right:0;top:38px"><span class="brand-dot"></span><span class="brand-name">Korvu.Ta</span></div>
  </div>
  <div class="abs info-blue" style="left:645px;top:399px;width:236px;height:343px"></div>
  <div class="abs back-slogan" style="left:670px;top:417px">o Bright Power at Every Door!<br>o Le Courant Clair Chez Chacun !</div>
  <div class="abs back-item" style="left:670px;top:460px">Battery capacity</div>
  <table class="abs spec-table" style="left:647px;top:479px">
    <tr><th>Setting</th><th>Light runtime after one sunny day<br>of solar charging</th><th>Brightness</th></tr>
    <tr><td>High</td><td>4 hrs</td><td>120 lumens</td></tr>
    <tr><td>Medium</td><td>8 hrs</td><td>100 lumens</td></tr>
    <tr><td>Low</td><td>16 hrs</td><td>50 lumens</td></tr>
    <tr><td>Red-light</td><td>60 hrs</td><td>10 lumens</td></tr>
  </table>
  <div class="abs back-item" style="left:670px;top:530px">Solar module capacity</div>
  <div class="abs back-item" style="left:670px;top:545px">Lightning brightness</div>
  <div class="abs back-note" style="left:672px;top:560px">- &gt; 20 lumens</div>
  <div class="abs back-note" style="left:672px;top:576px">- Illuminates a 0.1 m2 surface at ≥25 lux under conditions<br>defined by the QTM</div>
  <div class="abs back-item" style="left:670px;top:606px">Numbers of LEDs</div>
  <div class="abs back-item" style="left:670px;top:621px">Lights modes</div>
  <div class="abs back-item" style="left:670px;top:636px">USB port</div>
  <div class="abs back-item" style="left:670px;top:651px">Mobile Phone Charging</div>
  <div class="abs back-item" style="left:670px;top:666px">Warranty length in months</div>
  <div class="abs back-item" style="left:670px;top:681px">Battery deposit refund system</div>
  <div class="abs africa-note" style="left:676px;top:697px">Conception 100% Afrique /<br>100% Africa with Africa continent drawing</div>
  <div class="abs back-web" style="left:700px;top:721px">www.brevomarel.org</div>

  <div class="abs band-pink" style="left:645px;top:742px;width:236px;height:68px"></div>
  <svg class="abs" style="left:656px;top:754px" width="22" height="26" viewBox="0 0 22 26" aria-hidden="true">
    <rect x="4" y="5" width="14" height="16" fill="none" stroke="#222" stroke-width="1.5"/>
    <line x1="2" y1="5" x2="20" y2="5" stroke="#222" stroke-width="1.5"/>
    <line x1="2" y1="24" x2="20" y2="24" stroke="#222" stroke-width="2"/>
  </svg>
  <div class="abs origin-note" style="left:732px;top:762px">Fabriqué en RPC<br>Made in PRC</div>
  <div class="abs" style="left:812px;top:756px;width:24px;height:24px;border-radius:50%;border:3px solid #4f9a43"></div>

  <!-- runtime panel -->
  <div class="abs runtime-red" style="left:881px;top:298px;width:265px;height:444px"></div>
  <svg class="abs" style="left:881px;top:298px" width="265" height="110" viewBox="0 0 265 110">
    <polygon points="0,0 140,0 105,96 0,106" fill="#e1e5e8"/>
  </svg>
  <div class="abs runtime-title" style="left:910px;top:374px">Runtime</div>
  <div class="abs runtime-text" style="left:910px;top:408px;width:225px">
    To meet the runtime target, the product must provide either:<br><br>
    - &gt; 8 hours of light at greater than or equal to the specified light output<br>&nbsp;&nbsp;with a fully charged battery<br><br>
    - &gt; 4 hours of light at greater than or equal to the specified light output after<br>one day of solar charging as defined by the QTM (PV only)
  </div>
  <div class="abs" role="img" aria-label="Photo of the solar lantern glowing on a dark floor" style="left:899px;top:492px;width:150px;height:178px;background:radial-gradient(ellipse at 50% 88%,#e8e8e8 0%,#9a9a9a 28%,rgba(60,0,0,0) 55%),radial-gradient(ellipse at 50% 40%,#f2f2ee 0%,#e6dc8a 35%,rgba(245,200,20,.9) 55%,rgba(153,0,0,0) 72%)"></div>
  <svg class="abs" style="left:960px;top:520px" width="100" height="95" viewBox="0 0 100 95" aria-hidden="true">
    <line x1="10" y1="8" x2="92" y2="8" stroke="#fff" stroke-width=".8"/>
    <line x1="40" y1="33" x2="92" y2="33" stroke="#fff" stroke-width=".8"/>
    <line x1="45" y1="88" x2="100" y2="88" stroke="#fff" stroke-width=".8"/>
  </svg>
  <div class="abs callout" style="left:1054px;top:523px">Solar panel</div>
  <div class="abs callout" style="left:1054px;top:548px">Light</div>
  <div class="abs callout" style="left:1062px;top:603px">Switch</div>
  <div class="abs runtime-foot" style="left:910px;top:689px;width:225px">
    electricity source, most commonly a small 1-5W solar panel;<br>a modern rechargeable battery, increasingly lithium-ion; and<br>a modern lantern or lamp, usually with an LED (light emitting<br>diode) bulb.
  </div>
  <div class="abs band-pink" style="left:881px;top:742px;width:265px;height:68px"></div>

</div>
</body>
</html>
```